Business card design needed

We need a business card design and possible logo for my new building construction business. I would like a masculine type of business design.

Thanks
Also can we please put my ABN number 47380926514 in as well thanks.
And use the colours black, orange and white. Cheers

Industry/Entity Type

Building

Contact Information for Business Card

Tarrow constructions, owner: Derek hollis, mobile:0417282613, email: hollo.d@quenmail.com, licence: 618374K

```html
<!DOCTYPE html>
<html lang="en">
<head>
<meta charset="utf-8">
<title>Tarrow Constructions – Business Card</title>
<link rel="stylesheet" href="https://fonts.googleapis.com/css2?family=Open+Sans:wght@400;700&display=swap">
<style>
  :root {
    --canvas-bg: #e9e7e4;
    --card-black: #030303;
    --ink-white: #ffffff;
    --ink-soft: #e6e6e6;
    --deco-grey: #2a2a2a;
    --deco-grey-light: #3a3a3a;
    --rule-silver: #d8d8d8;
  }
  * { box-sizing: border-box; margin: 0; padding: 0; }
  html, body {
    width: 1200px;
    height: 1000px;
    overflow: hidden;
  }
  body {
    background: var(--canvas-bg);
    font-family: "Open Sans", Arial, sans-serif;
    position: relative;
  }
  .card {
    position: absolute;
    top: 350px;
    width: 535px;
    height: 300px;
    background: var(--card-black);
    box-shadow: 0 6px 18px rgba(0,0,0,0.35);
    overflow: hidden;
    color: var(--ink-white);
  }
  .card--front { left: 48px; }
  .card--back { left: 619px; }

  /* front */
  .holder-name {
    position: absolute;
    top: 34px;
    right: 42px;
    font-size: 20px;
    font-weight: 700;
    letter-spacing: 0.3px;
  }
  .brand-decoration {
    position: absolute;
    left: 205px;
    top: 90px;
    width: 310px;
    height: 210px;
    background: linear-gradient(135deg, var(--deco-grey) 0%, var(--deco-grey-light) 55%, var(--deco-grey) 100%);
    opacity: 0.55;
  }
  .brand-mark {
    position: absolute;
    display: flex;
    align-items: center;
    gap: 8px;
    font-weight: 700;
    color: var(--ink-white);
    text-transform: uppercase;
    white-space: nowrap;
  }
  .brand-mark__square {
    width: 14px;
    height: 14px;
    background: var(--ink-white);
    flex: none;
  }
  .card--front .brand-mark {
    left: 34px;
    bottom: 32px;
    font-size: 12.5px;
  }
  .contact-list {
    position: absolute;
    left: 316px;
    top: 202px;
    list-style: none;
    font-size: 14.5px;
    color: var(--ink-soft);
  }
  .contact-list li {
    display: flex;
    align-items: center;
    height: 24.5px;
  }
  .contact-icon {
    width: 17px;
    height: 17px;
    margin-right: 11px;
    flex: none;
  }

  /* back */
  .silver-rule {
    position: absolute;
    left: 70px;
    width: 395px;
    height: 3px;
    background: radial-gradient(ellipse at center, var(--rule-silver) 0%, rgba(216,216,216,0.5) 45%, rgba(216,216,216,0) 100%);
  }
  .silver-rule--top { top: 52px; }
  .silver-rule--bottom { top: 244px; }
  .card--back .brand-mark {
    left: 50%;
    top: 50%;
    transform: translate(-50%, -50%);
    font-size: 17px;
    gap: 10px;
  }
  .card--back .brand-mark__square {
    width: 18px;
    height: 18px;
  }
</style>
</head>
<body>

  <section class="card card--front" aria-label="Business card front">
    <div class="brand-decoration" role="img" aria-label="Faint enlarged brand symbol decoration"></div>
    <h1 class="holder-name">DEREK HOLLIS</h1>
    <div class="brand-mark">
      <span class="brand-mark__square" aria-hidden="true"></span>
      <span class="brand-mark__name">Tarrow Constructions</span>
    </div>
    <ul class="contact-list">
      <li>
        <svg class="contact-icon" viewBox="0 0 20 20" aria-hidden="true">
          <circle cx="10" cy="10" r="9" fill="none" stroke="#ffffff" stroke-width="1.6"/>
          <path d="M6.6 5.2c.4-.3.9-.3 1.2.1l1.2 1.6c.3.4.2.9-.1 1.2l-.7.6c.5 1.2 1.3 2.1 2.6 2.8l.6-.7c.3-.4.8-.4 1.2-.2l1.6 1.1c.4.3.5.8.2 1.2l-.6.8c-.5.6-1.3.8-2 .5-2.6-1-4.5-2.9-5.6-5.6-.3-.7-.1-1.5.4-2z" fill="#ffffff"/>
        </svg>
        <span>0417 282 613</span>
      </li>
      <li>
        <svg class="contact-icon" viewBox="0 0 20 20" aria-hidden="true">
          <circle cx="10" cy="10" r="9" fill="none" stroke="#ffffff" stroke-width="1.6"/>
          <text x="10" y="14" text-anchor="middle" font-size="12" font-weight="700" fill="#ffffff" font-family="Open Sans, Arial, sans-serif">@</text>
        </svg>
        <span>hollo.d@quenmail.com</span>
      </li>
      <li><span>Lic: 618374K</span></li>
    </ul>
  </section>

  <section class="card card--back" aria-label="Business card back">
    <div class="silver-rule silver-rule--top"></div>
    <div class="brand-mark">
      <span class="brand-mark__square" aria-hidden="true"></span>
      <span class="brand-mark__name">Tarrow Constructions</span>
    </div>
    <div class="silver-rule silver-rule--bottom"></div>
  </section>

</body>
</html>
```